Automotive component supplier needs a business card design

We need a business card design for our company called Velmar Global Components Ltd based in the UK. We are a supplier of interior and exterior components to premium car manufacturers such as Corvane Hale, Durrant Fyfe, Maxtorn and Valdessimo. We would like to see a modern business card design that uses the colour blue.

Target Market(s)

Premium automotive car manufacturers.

Industry/Entity Type

Automotive

Contact Information for Business Card

Company Name : Velmar Global Components Limited
Address: 17 Tamsey Yard, Upper Drisk, Warwick, CV31 8RJ, United Kingdom
Web Address : www.velmarparts-example.co.uk

Font styles to use
Other font styles liked:
• Helvetica

Colors
3176b5
0255a3
85acd3
cfdeed
cee9f5
85cae6
34a6d7
0692cd
9bcb3c

Requirements
Must have
• Clear company logo and a mixture of blue colours.
Nice to have
• A high quality modern image.
Should not have
• Multiple colours.

```html
<!DOCTYPE html>
<html lang="en">
<head>
<meta charset="utf-8">
<title>Velmar Global Components – Business Card</title>
<link rel="stylesheet" href="https://fonts.googleapis.com/css2?family=Arimo:wght@400;700&display=swap">
<style>
  :root {
    --bg: #2b2c2e;
    --white: #ffffff;
    --blue: #0692cd;
    --blue-light: #34a6d7;
    --blue-deep: #0255a3;
    --green: #9bcb3c;
    --ink: #3d3f42;
    --font: "Arimo", Helvetica, Arial, sans-serif;
  }
  * { box-sizing: border-box; margin: 0; padding: 0; }
  html, body {
    width: 1200px; height: 950px; overflow: hidden;
    background: var(--bg);
    font-family: var(--font);
  }
  .canvas {
    position: relative; width: 1200px; height: 950px;
  }
  .card {
    position: absolute; left: 250px; width: 700px; height: 400px;
    overflow: hidden;
  }
  .card--front { top: 50px; background: var(--white); }
  .card--back { top: 500px; background: var(--blue); }

  /* front */
  .brand {
    position: absolute; right: 56px; top: 42px; text-align: right;
    color: var(--blue); font-weight: 700; line-height: 1;
  }
  .brand__name { font-size: 58px; letter-spacing: 3px; }
  .brand__sub { font-size: 16px; letter-spacing: 1.5px; margin-top: 6px; }
  .divider {
    position: absolute; left: 40px; right: 40px; top: 156px;
    height: 1px; background: var(--blue-light);
  }
  .person { position: absolute; left: 48px; top: 188px; }
  .person__name { font-size: 25px; color: var(--blue-light); }
  .person__role { font-size: 17px; color: var(--green); margin-top: 4px; }
  .contacts {
    position: absolute; left: 48px; top: 256px; list-style: none;
    font-size: 15px; color: var(--ink);
  }
  .contacts li { display: flex; align-items: center; gap: 10px; height: 23px; }
  .contacts svg { width: 15px; height: 15px; fill: var(--ink); flex: none; }
  .address {
    position: absolute; right: 48px; top: 178px; text-align: right;
    font-size: 15px; line-height: 1.45; color: var(--ink); font-style: normal;
  }
  .edge {
    position: absolute; left: 0; right: 0; bottom: 0; height: 14px; display: flex;
  }
  .edge__blue { width: 58%; background: var(--blue); }
  .edge__green { flex: 1; background: var(--green); margin-left: 4px; }

  /* back */
  .back-brand {
    position: absolute; left: 0; right: 0; top: 118px; text-align: center;
    color: var(--white); font-weight: 700; line-height: 1;
  }
  .back-brand__name { font-size: 104px; letter-spacing: 6px; }
  .back-brand__sub { font-size: 24px; letter-spacing: 3px; margin-top: 10px; }
  .back-web {
    position: absolute; left: 0; right: 0; top: 302px; text-align: center;
    color: var(--white); font-size: 15px; letter-spacing: 4px;
  }
</style>
</head>
<body>
<main class="canvas">

  <section class="card card--front" aria-label="Business card front">
    <div class="brand">
      <div class="brand__name">VELMAR</div>
      <div class="brand__sub">GLOBAL COMPONENTS</div>
    </div>
    <div class="divider"></div>

    <div class="person">
      <div class="person__name">Dorian Vale</div>
      <div class="person__role">President</div>
    </div>

    <ul class="contacts">
      <li>
        <svg viewBox="0 0 16 16" aria-hidden="true"><path d="M3.6 1.2l2.3 2.7-1.3 1.8c.9 2 2.4 3.6 4.5 4.6l1.8-1.3 2.8 2.3-1.4 2.4C7.2 13.5 2.4 8.8 1.3 3z"/></svg>
        512 7304 6618
      </li>
      <li>
        <svg viewBox="0 0 16 16" aria-hidden="true"><path d="M4.5 1h7a1 1 0 0 1 1 1v12a1 1 0 0 1-1 1h-7a1 1 0 0 1-1-1V2a1 1 0 0 1 1-1zm.5 2v9h6V3zm3 10a.8.8 0 1 0 0 1.6A.8.8 0 0 0 8 13z"/></svg>
        847 2916 0473
      </li>
      <li>
        <svg viewBox="0 0 16 16" aria-hidden="true"><path d="M1 3.5h14v9H1zm1.4 1L8 8.6l5.6-4.1zM2 5.6V11.5h12V5.6L8 10z"/></svg>
        dorian@velmarparts-example.co.uk
      </li>
      <li>
        <svg viewBox="0 0 16 16" aria-hidden="true"><path d="M8 1a7 7 0 1 0 0 14A7 7 0 0 0 8 1zm0 1.5c.7 0 1.6 1.5 1.9 4.5H6.1C6.4 4 7.3 2.5 8 2.5zM2.6 8.5h2.1c.1 1.6.4 3 .9 4A5.5 5.5 0 0 1 2.6 8.5zm0-1.5a5.5 5.5 0 0 1 3-4c-.5 1-.8 2.4-.9 4zm5.4 6.5c-.7 0-1.6-1.5-1.9-5h3.8c-.3 3.5-1.2 5-1.9 5zm2.4-1c.5-1 .8-2.4.9-4h2.1a5.5 5.5 0 0 1-3 4zm.9-5.5c-.1-1.6-.4-3-.9-4a5.5 5.5 0 0 1 3 4z"/></svg>
        www.velmarparts-example.co.uk
      </li>
    </ul>

    <address class="address">
      17 Tamsey Yard, Upper Drisk<br>
      Warwick, CV31 8RJ<br>
      United Kingdom
    </address>

    <div class="edge"><div class="edge__blue"></div><div class="edge__green"></div></div>
  </section>

  <section class="card card--back" aria-label="Business card back">
    <div class="back-brand">
      <div class="back-brand__name">VELMAR</div>
      <div class="back-brand__sub">GLOBAL COMPONENTS</div>
    </div>
    <div class="back-web">www.velmarparts-example.co.uk</div>
  </section>

</main>
</body>
</html>
```